Brivane - Business Cards for a new venture

create business card for a startup classified business dealing in construction materials, the cards need to have a professional look but modern, more serious than playful, one of the samples must include the official font (attached), please explore using the official colors in the company's logo

Target Market(s)

Energy sector

Contact Information for Business Card

Font styles to use
Other font styles liked:
• suissnord

Requirements
Must have
• corporate colors (in logo attached)
Nice to have
• Official font (in one of the samples) font is : suissnord
Should not have
• Cartoonish look

```html
<!DOCTYPE html>
<html lang="en">
<head>
<meta charset="utf-8">
<title>Brivane — Business Cards</title>
<link href="https://fonts.googleapis.com/css2?family=Michroma&family=Roboto:wght@400&display=swap" rel="stylesheet">
<style>
  :root {
    --navy: #1b4179;
    --navy-deep: #173a6d;
    --white: #ffffff;
    --grey-mark: #8e9196;
    --frame: #e3e4e6;
    --backdrop: #2b2c2e;
  }
  * { box-sizing: border-box; margin: 0; padding: 0; }
  html, body { width: 1200px; height: 1040px; overflow: hidden; background: var(--backdrop); }
  .canvas { position: relative; width: 1200px; height: 1040px; }

  .card { position: absolute; left: 160px; width: 880px; height: 503px; }

  /* Front */
  .card-front { top: 16px; background: var(--navy); color: var(--white); }
  .card-front .wordmark {
    position: absolute; top: 190px; left: 0; right: 0; text-align: center;
    font-family: "Michroma", sans-serif; font-size: 58px; letter-spacing: 10px; color: var(--white);
  }
  .card-front .site {
    position: absolute; top: 330px; left: 0; right: 0; text-align: center;
    font-family: "Roboto", sans-serif; font-size: 20px; letter-spacing: 0.5px;
  }

  /* Back */
  .card-back { top: 521px; background: var(--white); padding: 22px; }
  .card-back .frame { position: absolute; inset: 0; border: 22px solid var(--frame); }
  .card-back .brand {
    position: absolute; left: 22px; top: 22px; width: 400px; bottom: 22px;
    display: flex; align-items: center; justify-content: center;
  }
  .card-back .brand .wordmark {
    font-family: "Michroma", sans-serif; font-size: 38px; letter-spacing: 6px; color: var(--grey-mark);
  }
  .card-back .panel {
    position: absolute; left: 432px; right: 22px; top: 22px; bottom: 48px;
    background: var(--navy); color: var(--white);
    padding: 70px 36px 0 52px; font-family: "Roboto", sans-serif;
  }
  .panel .name { font-family: "Michroma", sans-serif; font-size: 28px; letter-spacing: 1px; line-height: 1; }
  .panel .role { font-family: "Michroma", sans-serif; font-size: 17px; letter-spacing: 1px; margin-top: 6px; }
  .panel .address { margin-top: 40px; font-size: 19px; line-height: 1.3; }
  .panel .contacts { list-style: none; margin-top: 4px; font-size: 19px; line-height: 1.3; }
  .panel .contacts li { display: flex; align-items: center; gap: 10px; }
  .panel .contacts svg { width: 18px; height: 18px; flex: none; }
</style>
</head>
<body>
<main class="canvas">
  <section class="card card-front" aria-label="Business card front">
    <div class="wordmark">BRIVANE</div>
    <div class="site">www.evanmarlow.com</div>
  </section>

  <section class="card card-back" aria-label="Business card back">
    <div class="frame"></div>
    <div class="brand"><span class="wordmark">BRIVANE</span></div>
    <div class="panel">
      <div class="name">EVAN MARLOW</div>
      <div class="role">FOUNDER</div>
      <p class="address">Harbor City,Street No,<br>Zip Code,State, CA-123,NYC</p>
      <ul class="contacts">
        <li>
          <svg viewBox="0 0 24 24" fill="none" stroke="#fff" stroke-width="2.2" aria-hidden="true"><path d="M5 3h4l2 5-3 2a12 12 0 0 0 6 6l2-3 5 2v4a2 2 0 0 1-2 2A18 18 0 0 1 3 5a2 2 0 0 1 2-2z"/></svg>
          (555) 210-4400
        </li>
        <li>
          <svg viewBox="0 0 24 24" fill="none" stroke="#fff" stroke-width="2" aria-hidden="true"><rect x="6" y="2" width="12" height="20" rx="2"/><line x1="11" y1="18" x2="13" y2="18"/></svg>
          (555) 210-4401
        </li>
        <li>
          <svg viewBox="0 0 24 24" fill="none" stroke="#fff" stroke-width="2" aria-hidden="true"><rect x="2" y="5" width="20" height="14"/><path d="M2 5l10 8 10-8"/></svg>
          evan@marlow.com
        </li>
        <li>
          <svg viewBox="0 0 24 24" fill="none" stroke="#fff" stroke-width="1.8" aria-hidden="true"><circle cx="12" cy="12" r="10"/><ellipse cx="12" cy="12" rx="4" ry="10"/><line x1="2" y1="12" x2="22" y2="12"/><path d="M4 7h16M4 17h16"/></svg>
          www.evanmarlow.com
        </li>
      </ul>
    </div>
  </section>
</main>
</body>
</html>
```